Quorvex business card design

create modern and tech looking business card that is clean but effectively communciates that we are a cloud communications company.
Should have at minimum:
Employee Name
Postion
Phone Number
Email
website
create modern and tech looking business card that is clean but effectively communciates that we are a cloud communications company. We have two logo color schemes (attached) so would like to see designs both ways
Should have at minimum:
Employee Name
Postion
Phone Number
Email
website

```html
<!DOCTYPE html>
<html lang="en">
<head>
<meta charset="utf-8">
<title>Quorvex business card</title>
<link rel="stylesheet" href="https://fonts.googleapis.com/css2?family=Aldrich&display=swap">
<style>
  :root {
    --stage: #ece9e5;
    --card: #ffffff;
    --ink: #4b4b50;
    --purple: #5e2d8c;
    --purple-deep: #4a2679;
    --cyan: #2fbadf;
    --lavender: #ebe7f4;
  }
  * { margin: 0; padding: 0; box-sizing: border-box; }
  html, body { width: 900px; height: 1200px; overflow: hidden; }
  body {
    background: var(--stage);
    font-family: "Aldrich", "Segoe UI", sans-serif;
    position: relative;
  }
  .card {
    position: absolute;
    left: 55px;
    width: 788px;
    height: 462px;
    background: var(--card);
    overflow: hidden;
    box-shadow: 0 4px 14px rgba(0,0,0,.18);
  }
  .card--front { top: 118px; }
  .card--back { top: 631px; }

  .texture {
    position: absolute;
    inset: 0;
    background:
      radial-gradient(ellipse at 10% 10%, var(--lavender) 0, transparent 45%),
      radial-gradient(ellipse at 92% 85%, var(--lavender) 0, transparent 50%);
  }

  .wordmark {
    position: absolute;
    display: flex;
    align-items: center;
    gap: 18px;
    color: var(--ink);
    text-transform: uppercase;
    letter-spacing: 2px;
    line-height: 1;
  }
  .wordmark__square {
    width: 30px;
    height: 30px;
    background: var(--purple);
  }
  .card--front .wordmark { left: 170px; top: 198px; font-size: 60px; }
  .card--back .wordmark { left: 45px; top: 92px; font-size: 46px; }
  .card--back .wordmark__square { width: 24px; height: 24px; }

  .name-band {
    position: absolute;
    left: 0;
    top: 231px;
    width: 380px;
    height: 75px;
    background: var(--purple);
    padding: 12px 0 0 42px;
  }
  .name-band__name {
    color: #fff;
    font-size: 29px;
    letter-spacing: 1.5px;
    line-height: 1;
  }
  .name-band__role {
    color: var(--cyan);
    font-size: 17px;
    margin-top: 6px;
    letter-spacing: .5px;
  }

  .contact {
    position: absolute;
    left: 43px;
    top: 334px;
    list-style: none;
  }
  .contact__item {
    display: flex;
    align-items: center;
    gap: 12px;
    height: 32.5px;
    color: var(--purple-deep);
    font-size: 22px;
    letter-spacing: .5px;
  }
  .contact__icon {
    width: 23px;
    height: 23px;
    flex: none;
  }

  .accent-field {
    position: absolute;
    right: 0;
    top: 0;
    width: 250px;
    height: 462px;
    background: linear-gradient(180deg, rgba(47,186,223,.55) 0%, rgba(47,186,223,.25) 50%, rgba(94,45,140,.45) 100%);
  }
</style>
</head>
<body>

<section class="card card--front">
  <div class="texture" role="img" aria-label="Faint scattered lavender squares across the card"></div>
  <div class="wordmark"><span class="wordmark__square"></span>Quorvex</div>
</section>

<section class="card card--back">
  <div class="texture" role="img" aria-label="Faint scattered lavender squares across the card"></div>
  <div class="accent-field" role="img" aria-label="Large cyan and purple brand decoration"></div>

  <div class="wordmark"><span class="wordmark__square"></span>Quorvex</div>

  <div class="name-band">
    <p class="name-band__name">DANIEL HALE</p>
    <p class="name-band__role">Managing Director</p>
  </div>

  <ul class="contact">
    <li class="contact__item">
      <svg class="contact__icon" viewBox="0 0 23 23" aria-hidden="true"><rect width="23" height="23" fill="#5e2d8c"/><path d="M6 8c0-2 3-2 5.5-2S17 6 17 8l-2 1c-1-1-6-1-7 0z M8 11h7l1 6H7z" fill="#fff"/></svg>
      555-014-0192
    </li>
    <li class="contact__item">
      <svg class="contact__icon" viewBox="0 0 23 23" aria-hidden="true"><rect width="23" height="23" fill="#5e2d8c"/><rect x="5" y="7" width="13" height="9" fill="none" stroke="#fff" stroke-width="1.4"/><path d="M5 7l6.5 5L18 7" fill="none" stroke="#fff" stroke-width="1.4"/></svg>
      daniel@quorvex.com
    </li>
    <li class="contact__item">
      <svg class="contact__icon" viewBox="0 0 23 23" aria-hidden="true"><rect width="23" height="23" fill="#5e2d8c"/><circle cx="11.5" cy="11.5" r="6" fill="none" stroke="#fff" stroke-width="1.3"/><ellipse cx="11.5" cy="11.5" rx="2.6" ry="6" fill="none" stroke="#fff" stroke-width="1.1"/><path d="M5.5 11.5h12" stroke="#fff" stroke-width="1.1"/></svg>
      www.quorvex.com
    </li>
  </ul>
</section>

</body>
</html>
```